Post Disaster Temporary Housing Literature Review poster

Wanting a poster design for two Emergency Management conferences we have coming up. The information to be included in the poster is capturing the purpose, findings and recommendations from a post disaster temporary housing literature review looking at “What should government consider in order to improve planning and decision making for accommodation needs after a disaster, and to support people’s transition to stable housing?”
I’d like to enhance the visual appeal through including relevant images or graphic. I am also open to reducing the text if needed.
The government group I work with focuses on the social and human side of disaster recovery so keen for any images to reflect the human aspect and not focus solely on disasters or housing.
Government and NGO's

```html
<!DOCTYPE html>
<html lang="en">
<head>
<meta charset="utf-8">
<title>Post Disaster Temporary Housing – Literature Review Poster</title>
<link rel="stylesheet" href="https://fonts.googleapis.com/css2?family=Montserrat:wght@600;700;800&family=Nunito:wght@600;700;800&display=swap">
<style>
  :root {
    --page-bg: #ececec;
    --paper: #ffffff;
    --sky: #1fa9e8;
    --sky-light: #3cc0f2;
    --sky-deep: #0d7fc8;
    --navy: #0b3f78;
    --navy-dark: #0a2244;
    --heading-navy: #23337a;
    --list-blue: #1d9fe0;
    --photo-dark: #3b3a36;
    --photo-light: #b7a98a;
  }
  * { margin: 0; padding: 0; box-sizing: border-box; }
  html, body { width: 1200px; height: 1000px; overflow: hidden; }
  body { background: var(--page-bg); position: relative; }

  .poster {
    position: absolute; left: 270px; top: 33px;
    width: 660px; height: 935px;
    background: var(--paper);
    overflow: hidden;
  }
  .poster-shapes { position: absolute; inset: 0; }

  .org-name {
    position: absolute; left: 32px; top: 40px;
    font-family: "Nunito", sans-serif; font-weight: 800;
    font-size: 19px; line-height: 22px; color: #fff;
  }

  .title { position: absolute; left: 24px; color: #fff; font-family: "Montserrat", sans-serif; }
  .title-post { top: 425px; font-size: 84px; font-weight: 800; line-height: 1; letter-spacing: 1px; }
  .title-disaster { top: 500px; font-size: 44px; font-weight: 800; line-height: 1; }
  .title-subject { top: 553px; left: 27px; font-size: 15px; font-weight: 700; letter-spacing: 4.6px; }
  .title-review { top: 575px; font-size: 33px; font-weight: 700; letter-spacing: 0.5px; }

  .recommendations { position: absolute; left: 38px; top: 652px; font-family: "Nunito", sans-serif; }
  .recommendations h2 { font-size: 21px; font-weight: 800; color: var(--heading-navy); margin-bottom: 22px; }
  .recommendations ol { list-style: none; color: var(--list-blue); font-size: 21px; font-weight: 700; line-height: 24.7px; }

  .contact-bar {
    position: absolute; left: 0; bottom: 0; width: 660px; height: 53px;
    display: flex; align-items: center; justify-content: space-around;
    padding: 0 30px 0 40px;
    font-family: "Nunito", sans-serif; font-weight: 600; font-size: 16px; color: #fff;
  }
  .contact-item { display: flex; align-items: center; gap: 8px; }
  .contact-item svg { width: 18px; height: 18px; }
</style>
</head>
<body>
  <main class="poster">
    <svg class="poster-shapes" width="660" height="935" viewBox="0 0 660 935">
      <defs>
        <linearGradient id="heroBlue" x1="0" y1="0" x2="1" y2="1">
          <stop offset="0" stop-color="#0f86d0"/>
          <stop offset="0.5" stop-color="#2fb5ee"/>
          <stop offset="1" stop-color="#11a0e4"/>
        </linearGradient>
        <linearGradient id="tagBlue" x1="0" y1="0" x2="1" y2="0">
          <stop offset="0" stop-color="#1c97e0"/>
          <stop offset="1" stop-color="#41c3f3"/>
        </linearGradient>
        <linearGradient id="photoTone" x1="0" y1="0" x2="1" y2="1">
          <stop offset="0" stop-color="#d9d6c8"/>
          <stop offset="0.35" stop-color="#6d6655"/>
          <stop offset="0.7" stop-color="#4a3a30"/>
          <stop offset="1" stop-color="#2f3a3a"/>
        </linearGradient>
        <linearGradient id="barNavy" x1="0" y1="0" x2="1" y2="0">
          <stop offset="0" stop-color="#0c4a8c"/>
          <stop offset="1" stop-color="#0a2244"/>
        </linearGradient>
        <linearGradient id="stripBlue" x1="0" y1="0" x2="1" y2="1">
          <stop offset="0" stop-color="#5cc8f0"/>
          <stop offset="1" stop-color="#0b5fa8"/>
        </linearGradient>
      </defs>

      <!-- hero blue field -->
      <path class="hero-field" d="M0,150 L660,150 L660,790 L520,640 C440,615 200,615 0,635 Z" fill="url(#heroBlue)"/>
      <!-- diagonal accent strip -->
      <path class="accent-strip" d="M500,618 C540,630 560,640 590,672 L660,750 L660,790 L560,690 C535,660 520,645 500,640 Z" fill="url(#stripBlue)"/>
      <!-- dark accent wedge -->
      <path class="accent-wedge" d="M0,168 L110,300 C120,315 125,325 130,336 L0,336 Z" fill="#0d5fa6"/>

      <!-- white frame behind photo -->
      <path class="photo-frame" d="M320,10 L660,10 L660,420 L238,420 C205,420 188,408 170,388 L0,185 L0,150 C10,140 20,132 30,128 L290,128 Z" fill="#ffffff"/>
      <!-- photo: house among trees -->
      <path class="photo" role="img" aria-label="Photo of a timber house with a grey roof among trees in soft morning light"
            d="M335,22 L635,22 L635,397 L245,397 C215,397 200,390 185,372 L18,172 C30,160 40,152 60,150 L300,150 Z"
            fill="url(#photoTone)"/>

      <!-- organisation tag -->
      <path class="org-tag" d="M12,22 L305,22 L262,112 C256,124 248,130 234,130 L12,130 Z" fill="url(#tagBlue)"/>

      <!-- growth chart icon -->
      <g class="chart-icon" fill="none" stroke="#fff" stroke-width="7">
        <path d="M540,478 L480,478 L480,583 L596,583 L596,545"/>
      </g>
      <g class="chart-bars" fill="#fff">
        <rect x="503" y="520" width="27" height="56"/>
        <rect x="538" y="497" width="27" height="56"/>
        <path d="M574,540 L574,471 L559,471 L589,436 L619,471 L604,471 L604,540 Z"/>
      </g>

      <!-- contact bar -->
      <rect class="footer-band" x="0" y="882" width="660" height="53" fill="url(#barNavy)"/>
    </svg>

    <div class="org-name">Community Renewal<br>Network<br>Australia</div>

    <div class="title title-post">POST</div>
    <div class="title title-disaster">DISASTER</div>
    <div class="title title-subject">TEMPORARY HOUSING</div>
    <div class="title title-review">LITERATURE REVIEW</div>

    <section class="recommendations">
      <h2>Recommendations</h2>
      <ol>
        <li>1.Terminology</li>
        <li>2.&nbsp; Post Disaster Temporary Housing Principles</li>
        <li>3.National Principles for Disaster Recovery</li>
        <li>4.&nbsp; Guidelines</li>
        <li>5. Capacity Building</li>
        <li>6.&nbsp; Funding</li>
        <li>7.&nbsp; Further Research</li>
      </ol>
    </section>

    <footer class="contact-bar">
      <span class="contact-item">
        <svg viewBox="0 0 24 24" aria-hidden="true"><path fill="#fff" d="M6.6 10.8a15.1 15.1 0 0 0 6.6 6.6l2.2-2.2a1 1 0 0 1 1-.25 11.4 11.4 0 0 0 3.6.57 1 1 0 0 1 1 1V20a1 1 0 0 1-1 1A17 17 0 0 1 3 4a1 1 0 0 1 1-1h3.5a1 1 0 0 1 1 1c0 1.25.2 2.45.57 3.57a1 1 0 0 1-.25 1z"/></svg>
        100-5550-1234-56
      </span>
      <span class="contact-item">
        <svg viewBox="0 0 24 24" aria-hidden="true"><path fill="#fff" d="M2 9l10-6 10 6v11H2z"/><path fill="#0b3a70" d="M2 9l10 6 10-6v2l-10 6L2 11z"/></svg>
        hello@renewalnet.org
      </span>
      <span class="contact-item">
        <svg viewBox="0 0 24 24" aria-hidden="true" fill="none" stroke="#fff" stroke-width="2"><circle cx="12" cy="12" r="9.5"/><ellipse cx="12" cy="12" rx="4" ry="9.5"/><path d="M2.5 12h19M4 7h16M4 17h16"/></svg>
        www.renewalnet.org
      </span>
    </footer>
  </main>
</body>
</html>
```